Book Cover for Fitness Trainer for Men

My name is Mabel Joy Crane. I am a female Fitness Trainer for Men.
I need a new Book Cover Design for my second book and a back of the book.
Both with updated text.
#A… Book Cover… I like the bright red and yellow colors.
I like the weight rack and the bold headline Font
#B… Book Cover…I like the full frontal sexier body. I don not like the font style.
I want the new design sexier; super sexy. Even more eye catching for guys.
I want to push the envelope to the point of almost too much sexy.
An Brindlo book 6”x9”, 150 pages

Target Market(s)

Men

Industry/Entity Type

Health and fitness for men

Colors
FFF300
FFF600
FEFA6F
FFFEC7
FFFEE8
EB3D1F
EC4F4E
F09395
F8D3D4
FCEDEE

Requirements
Must have
• Sexy & eye catching.

```html
<!DOCTYPE html>
<html lang="en">
<head>
<meta charset="utf-8">
<title>Fitness Trainer For Men – Book Cover Wrap</title>
<link rel="stylesheet" href="https://fonts.googleapis.com/css2?family=Anton&family=Bebas+Neue&family=Roboto:wght@400;700&family=Yellowtail&display=block">
<style>
  :root {
    --stage: #e9bfe3;
    --ink: #000000;
    --charcoal: #1c1c1c;
    --red: #eb1a12;
    --red-deep: #a80b0b;
    --yellow: #fff300;
    --white: #ffffff;
    --text-soft: #f2f2f2;
    --rule: #3a3a3a;
  }
  * { box-sizing: border-box; margin: 0; padding: 0; }
  html, body { width: 1200px; height: 2558px; overflow: hidden; }
  body { background: var(--stage); position: relative; font-family: "Roboto", sans-serif; }

  .wrap {
    position: absolute; left: 0; top: 871px;
    width: 1200px; height: 816px; background: var(--ink); overflow: hidden;
  }

  /* Back cover */
  .back { position: absolute; left: 0; top: 0; width: 585px; height: 816px; }
  .back-copy {
    position: absolute; left: 40px; top: 68px; width: 506px;
    color: var(--text-soft); font-size: 11.4px; line-height: 13.7px; text-align: center;
  }
  .back-copy p { margin: 0 auto 13px; }
  .back-copy .narrow { width: 380px; }
  .back-copy .mid { width: 400px; }
  .back-copy strong { font-weight: 700; }
  .back-copy .lead { font-size: 14.5px; line-height: 16px; margin-bottom: 1px; }
  .back-copy .claim { font-size: 13px; font-weight: 700; line-height: 15px; }
  .back-copy .tight { margin-bottom: 0; }
  .author-card { position: absolute; left: 236px; top: 585px; width: 112px; height: 120px; }
  .author-card .accent { position: absolute; left: 2px; top: 6px; width: 104px; height: 110px; background: var(--red); transform: rotate(-5deg); }
  .author-photo {
    position: absolute; left: 8px; top: 0; width: 100px; height: 112px;
    background: linear-gradient(160deg, #d9c2a8 0%, #b88d6a 45%, #2f4a47 100%);
  }
  .author-name {
    position: absolute; left: 0; width: 585px; top: 718px; text-align: center;
    color: var(--yellow); font-size: 11.5px; line-height: 13px;
  }
  .back-close {
    position: absolute; left: 0; width: 585px; top: 758px; text-align: center;
    color: var(--text-soft); font-size: 11.5px;
  }

  /* Spine */
  .spine {
    position: absolute; left: 585px; top: 0; width: 35px; height: 816px;
    border-left: 1px solid var(--rule); border-right: 1px solid var(--rule);
  }
  .spine-title {
    position: absolute; left: 50%; top: 200px; width: 446px;
    transform-origin: 0 0; transform: rotate(90deg) translate(0, -50%);
    color: var(--white); font-family: "Roboto", sans-serif; font-size: 21px;
    letter-spacing: 9.3px; white-space: nowrap; line-height: 1;
  }

  /* Front cover */
  .front { position: absolute; left: 620px; top: 0; width: 580px; height: 816px; }
  .cover-photo {
    position: absolute; left: 0; top: 0; width: 390px; height: 560px;
    background: radial-gradient(ellipse at 45% 45%, #b07a52 0%, #7a4a2c 40%, #2a1a12 75%, #000 100%);
  }
  .cover-shapes { position: absolute; left: 0; top: 0; }

  .brand { position: absolute; right: 18px; top: 36px; display: flex; align-items: center; gap: 8px; }
  .brand-dot { width: 34px; height: 34px; border-radius: 50%; background: var(--white); }
  .brand-name { font-size: 14px; font-weight: 400; color: var(--white); letter-spacing: 1px; }

  .badge {
    position: absolute; left: 355px; top: 146px; width: 150px; height: 150px; border-radius: 50%;
    background: var(--ink);
  }

  .author-mark {
    position: absolute; right: 14px; top: 326px; white-space: nowrap;
    font-family: "Anton", sans-serif; font-size: 62px; line-height: 1; color: var(--white);
    -webkit-text-stroke: 3px var(--red); paint-order: stroke fill;
    text-shadow: 4px 4px 0 var(--red);
  }
  .promise {
    position: absolute; right: 27px; top: 412px; text-align: right;
    color: var(--white); font-size: 20.5px; line-height: 26.7px;
  }
  .promise p + p { margin-top: 8px; }

  .headline {
    position: absolute; left: 30px; top: 548px; white-space: nowrap;
    font-family: "Anton", sans-serif; font-size: 148px; line-height: 1;
    color: var(--white); letter-spacing: 12px; font-weight: 400;
  }
  .subhead {
    position: absolute; left: 100px; top: 640px; white-space: nowrap;
    font-family: "Yellowtail", cursive; font-size: 66px; line-height: 1;
    color: var(--yellow); transform: rotate(-3deg);
    -webkit-text-stroke: 4px var(--red); paint-order: stroke fill;
  }
  .proof { position: absolute; left: 94px; top: 756px; width: 400px; height: 50px; }
  .proof-frame { position: absolute; left: 0; top: 0; }
  .proof-kicker {
    position: absolute; left: 0; width: 400px; top: 2px; text-align: center;
    font-family: "Bebas Neue", sans-serif; font-size: 22px; line-height: 1; color: var(--white);
  }
  .proof-line {
    position: absolute; left: 0; width: 400px; top: 28px; text-align: center;
    font-family: "Bebas Neue", sans-serif; font-size: 22px; line-height: 1; color: var(--white);
  }
</style>
</head>
<body>
<main class="wrap">

  <section class="back">
    <div class="back-copy">
      <p class="narrow">I've been using eye candy to get guys interested in health and fitness since the day I walked in the gym and turned heads. I figured if you wanted Tits &amp; Ass I'd give it to you. Enough to make a buck and get my guys healthier. As a personal fitness trainer for Men I've learned…that not all Guys are the same. Each of you is different and You need to find what works for You. When you do … the the pounds melt away, your gut shrinks, and your health improves.</p>
      <p>You'll love the new you. Your girl friend will love it. Your wife will love it.<br>Nothing a woman loves more than a long rock hard man in shape.</p>
      <p class="mid">While everybody in the fitness community screams and yells about gym memberships, 30 day challenges, and complete diet changes …<br>My Guys don't do all that. My Guys are Real Men with Real bodies.<br>Real Men that work for a living and don't have time to live in the gym.</p>
      <p>Real men are tired of gym rats with "Look at me" egos, God given<br>1% body fat and abs you'll never get. These guys are full of Shit! And<br>they're the first one to buy my book. Ya gotta love it.</p>
      <p class="lead">You need to find what works for you.</p>
      <p class="mid">"I made a few adjustment in my meals added a minimum amount of exercise and lost 17 pounds in three months. Thanks Mabel. Couldn't have done it without you."</p>
      <p class="tight">"<strong>Mabel I took your bait</strong> and it actually made sense. Can't believe you got me exercising.<br>My gut shrunk and had to buy new pants. Best 20 bucks I ever spent."<br>"<strong>I've tried a few expensive</strong> 30day programs but your <strong>Ultimate Workout</strong> was all I ever needed. You're right <strong>No F**king secret here.</strong>" "<strong>Strategically eating Fast food</strong> is genius. Never thought I could still eat "the good stuff" and lose weight. WOW!"<br>"<strong>My increasing weight</strong> was scaring the hell out of me. Showing me that it's the little changes I can do…that has changed everything." "<strong>Everybody wanted me to make big</strong> drastic changes in my life. I can't do that. All these little "Tricks of the Trade" I can do.<br>" Thank you Mabel."</p>
      <p class="claim tight">Real Men can be fit, healthy and in shape no matter their size, weight, or body fat.</p>
      <p class="tight">My mission is to get your lazy ass in shape by finding what works for you.<br>If I need to get your attention first…Then that's what I'll do.</p>
    </div>
    <div class="author-card">
      <div class="accent"></div>
      <div class="author-photo" role="img" aria-label="Portrait photo of the author, a smiling woman with long blonde hair"></div>
    </div>
    <div class="author-name">Mabel Joy Crane<br>Fitness Trainer for Men</div>
    <div class="back-close">Think you can do Twenty bucks to Get You Hot, Sweaty, and Hard?</div>
  </section>

  <section class="spine">
    <div class="spine-title">FITNESS TRAINER FOR MEN</div>
  </section>

  <section class="front">
    <div class="cover-photo" role="img" aria-label="Photo of a toned woman's torso in a black bra and briefs, glistening skin"></div>
    <svg class="cover-shapes" width="580" height="816" viewBox="0 0 580 816" aria-hidden="true">
      <defs>
        <linearGradient id="redFade" x1="1" y1="0" x2="0" y2="1">
          <stop offset="0" stop-color="#b10d0d"/>
          <stop offset="0.45" stop-color="#eb1a12"/>
          <stop offset="1" stop-color="#ff2a14"/>
        </linearGradient>
      </defs>
      <polygon points="370,0 580,0 580,150 500,200" fill="#1c1c1c"/>
      <polygon points="580,130 580,816 300,816 200,680 250,556 330,470 470,250" fill="url(#redFade)"/>
      <polygon points="0,560 545,548 575,572 575,662 545,691 0,691" fill="#000"/>
    </svg>

    <div class="brand">
      <span class="brand-dot"></span>
      <span class="brand-name">IRONVALE FIT</span>
    </div>

    <div class="badge" aria-hidden="true"></div>

    <div class="author-mark">MABEL JOY CRANE</div>

    <div class="promise">
      <p>HELPING GUYS GET<br>HOT, SWEATY, &amp; HARD</p>
      <p>SO POUNDS MELT AWAY,<br>YOUR GUT SHRINKS,<br>&amp; YOU LAST LONGER.</p>
    </div>

    <h1 class="headline">FITNESS</h1>
    <div class="subhead">Trainer For Men</div>

    <div class="proof">
      <svg class="proof-frame" width="400" height="50" viewBox="0 0 400 50" aria-hidden="true">
        <polyline points="110,3 0,3 0,36 20,36" fill="none" stroke="#fff300" stroke-width="2"/>
        <polyline points="290,3 398,3 398,36 378,36" fill="none" stroke="#fff300" stroke-width="2"/>
      </svg>
      <div class="proof-kicker">DOZEN OF SUCCESS</div>
      <div class="proof-line">STORIES FROM REAL GUYS WITH REAL RESULTS</div>
    </div>
  </section>

</main>
</body>
</html>
```